Tervolan Pty Ltd professional business card

A professional business card template using the colours from the supplied logo.
Clean crisp lines while, Modern while not being over the top.

Target Market(s)

Construction, commerical and industrial

Industry/Entity Type

Communications

Contact Information for Business Card

For a Communications, IT, Optical fibre installation company

Colors
37b8a4

```html
<!DOCTYPE html>
<html lang="el">
<head>
<meta charset="utf-8">
<title>Tervolan Stationery</title>
<link rel="stylesheet" href="https://fonts.googleapis.com/css2?family=Noto+Sans:wght@400;500&display=swap">
<style>
  :root {
    --backdrop: #e4e5e8;
    --paper: #ffffff;
    --teal: #16909f;
    --grey: #6d6e71;
    --ink: #2b2b2b;
    --window: #d4edfb;
  }
  * { margin: 0; padding: 0; box-sizing: border-box; }
  html, body { width: 1200px; height: 908px; overflow: hidden; }
  body {
    background: var(--backdrop);
    position: relative;
    font-family: "Noto Sans", Arial, sans-serif;
  }
  .wordmark {
    position: absolute;
    font-family: "Noto Sans", Arial, sans-serif;
    font-weight: 500;
    letter-spacing: 0.5px;
    line-height: 1;
    white-space: nowrap;
  }
  /* Letterhead */
  .letterhead {
    position: absolute; left: 310px; top: 38px;
    width: 382px; height: 540px;
    background: var(--paper);
    overflow: hidden;
  }
  .letterhead .wordmark { left: 225px; top: 34px; font-size: 21px; color: var(--grey); }
  .letter-block {
    position: absolute; left: 46px; width: 290px;
    font-size: 5.8px; line-height: 9.8px; color: var(--ink);
  }
  .footer-band { position: absolute; left: 0; bottom: 0; width: 100%; }
  /* Cards */
  .card {
    position: absolute; left: 738px; width: 155px; height: 100px;
    overflow: hidden;
  }
  .card .wordmark { left: 10px; top: 35px; font-size: 26px; }
  .card--teal { top: 38px; background: var(--teal); }
  .card--teal .wordmark { color: #fff; }
  .card--grey { top: 184px; background: var(--grey); }
  .card--grey .wordmark { color: #fff; }
  .card--white { top: 330px; background: var(--paper); }
  .card--white .wordmark { color: var(--grey); }
  .card--back { top: 477px; background: var(--paper); }
  .card--back .wordmark { left: 32px; top: 9px; font-size: 13px; color: var(--grey); }
  .card-shapes { position: absolute; inset: 0; }
  .card-text {
    position: absolute; color: #fff;
    font-family: Arial, "Noto Sans", sans-serif;
    font-size: 4.8px; line-height: 6.2px;
  }
  .card-text .person { font-size: 6px; line-height: 6px; }
  /* Envelope */
  .envelope {
    position: absolute; left: 310px; top: 624px;
    width: 416px; height: 208px;
    background: var(--paper); overflow: hidden;
  }
  .envelope .wordmark { left: 14px; top: 24px; font-size: 24px; color: var(--grey); }
  .address-window {
    position: absolute; left: 37px; top: 91px;
    width: 200px; height: 73px; background: var(--window);
  }
</style>
</head>
<body>

<section class="letterhead">
  <div class="wordmark">Tervolan</div>

  <p class="letter-block" style="top:73px">Το όνομά σας<br>Οδός και αριθμός<br>Πόλη, Νομός, Ταχ. κώδικας<br>Ημερομηνία</p>

  <p class="letter-block" style="top:127px">Όνομα παραλήπτη<br>Τίτλος<br>Όνομα σχολείου<br>Οδός και αριθμός<br>Πόλη, Νομός, Ταχ. κώδικας</p>

  <p class="letter-block" style="top:190px">Αγαπητέ/ή Όνομα παραλήπτη:</p>

  <p class="letter-block" style="top:206px">Έχω υποβάλει αίτηση για μια θέση βασικού επιπέδου ως θέση εργασίας στην Εταιρική<br>επωνυμία και θα χρειαστώ μια συστατική επιστολή. Θα με τιμούσατε εάν μπορούσατε να<br>γράψετε μια συστατική επιστολή για εμένα. Το μάθημά σας, Τίτλος μαθήματος, ήταν ένα από<br>τα αγαπημένα μου μαθήματα στη σχολή.</p>

  <p class="letter-block" style="top:253px">Εσωκλείω αντίτυπα του βιογραφικού μου σημειώματος και της βαθμολογίας μου για<br>ανασκόπηση. Θα δείτε ότι αποφοίτησα με μέσος όρος βαθμολογίας ΓΜΟ και ότι έχω εισαχθεί<br>σε αρκετούς ομίλους αριστούχων που ανταμείβουν την αριστεία στους τομείς του περιγραφή<br>τομέων αριστείας. Πέρα από αυτές τις διακρίσεις, διαθέτω επίσης εμπειρία στον τομείς<br>εμπειρίας από την καλοκαιρινή πρακτική μου άσκηση στην Εταιρική επωνυμία.</p>

  <p class="letter-block" style="top:311px">Εάν πιστεύετε ότι γνωρίζετε αρκετά για την εκπαίδευσή μου και τις δεξιότητές μου ώστε να<br>γράψετε μια συστατική επιστολή για εμένα, επικοινωνήστε μαζί μου τηλεφωνικώς στο αριθμός<br>τηλεφώνου ή μέσω ηλεκτρονικού ταχυδρομείου στη διεύθυνση διεύθυνση email. Θα σας<br>αποστείλω έναν φάκελο με προπληρωμένο τέλος, με τον οποίο μπορείτε να στείλετε τη<br>συστατική επιστολή σας.</p>

  <p class="letter-block" style="top:368px">Όποια κι αν είναι η απόφασή σας, σας ευχαριστώ θερμά για τον χρόνο σας και για την εξέταση<br>του αιτήματός μου.</p>

  <p class="letter-block" style="top:395px">Με εκτίμηση,</p>
  <p class="letter-block" style="top:436px">Το όνομά σας</p>
  <p class="letter-block" style="top:458px">Εσωκλείεται</p>

  <svg class="footer-band" width="382" height="34" viewBox="0 0 382 34" aria-hidden="true">
    <polygon points="182,34 236,0 382,0 382,34" fill="var(--grey)"/>
    <polygon points="0,0 164,0 199,34 0,34" fill="var(--teal)"/>
  </svg>
</section>

<section class="card card--teal"><div class="wordmark">Tervolan</div></section>
<section class="card card--grey"><div class="wordmark">Tervolan</div></section>
<section class="card card--white"><div class="wordmark">Tervolan</div></section>

<section class="card card--back">
  <svg class="card-shapes" width="155" height="100" viewBox="0 0 155 100" aria-hidden="true">
    <polygon points="51,50 155,0 155,100 103,100" fill="var(--grey)"/>
    <polygon points="0,0 103,100 0,100" fill="var(--teal)"/>
  </svg>
  <div class="wordmark">Tervolan</div>
  <p class="card-text" style="left:10px; top:58px">0123- 123456</p>
  <p class="card-text" style="left:10px; top:70px">info@tervolan.com<br>tervolan.com</p>
  <p class="card-text" style="left:98px; top:51px"><span class="person">Name Manager</span><br>manager</p>
  <p class="card-text" style="left:98px; top:71px">De Streetname12<br>1234 AA The City</p>
</section>

<section class="envelope">
  <div class="wordmark">Tervolan</div>
  <div class="address-window"></div>
  <svg class="footer-band" width="416" height="13" viewBox="0 0 416 13" aria-hidden="true">
    <polygon points="202,13 220,0 416,0 416,13" fill="var(--grey)"/>
    <polygon points="0,0 200,0 212,13 0,13" fill="var(--teal)"/>
  </svg>
</section>

</body>
</html>
```